Veridan Crest Business Cards

Veridan Crest Prestige Portfolio Group is a global representation business focusing on high end luxury. We need business cards to epitomize our global, luxury delivery model.

Target Market(s)

Global Representation in the hospitality industry

Industry/Entity Type

Hospitality

Contact Information for Business Card

name
title
email: first.last@vc-ppg.com
web: www.vc-ppg.com
mobile:

Requirements
Must have
• double sided design
• incorporate logo colours
• have logo prominent
Should not have
• no designs not incorporating logo colours.

```html
<!DOCTYPE html>
<html lang="en">
<head>
<meta charset="utf-8">
<title>Veridan Crest Business Cards</title>
<link href="https://fonts.googleapis.com/css2?family=Tinos:wght@400;700&display=swap" rel="stylesheet">
<style>
  :root {
    --gold: #9c8748;
    --gold-deep: #8a7640;
    --paper: #ffffff;
    --backdrop: #e8e3d8;
    --serif: "Tinos", "Times New Roman", serif;
  }
  * { margin: 0; padding: 0; box-sizing: border-box; }
  html, body {
    width: 1200px; height: 780px; overflow: hidden;
    background: var(--backdrop);
    font-family: var(--serif);
  }
  .sheet {
    position: relative; width: 1200px; height: 780px;
    display: flex; align-items: center; justify-content: center; gap: 50px;
  }
  .card {
    position: relative; width: 525px; height: 300px;
    background: var(--paper);
    box-shadow: 0 10px 28px rgba(60, 45, 20, 0.18);
    overflow: hidden;
  }
  .card-shape { position: absolute; inset: 0; width: 100%; height: 100%; }
  .card-shape .band { fill: var(--gold); }

  .front-brand {
    position: absolute; top: 58px; right: 118px;
    color: var(--gold); font-size: 30px; font-weight: 400;
    letter-spacing: 1px;
  }
  .contact {
    position: absolute; left: 132px; top: 148px;
    color: var(--gold);
  }
  .contact-name { font-size: 17px; font-weight: 700; letter-spacing: 0.5px; }
  .contact-title { font-size: 13px; margin-bottom: 12px; }
  .contact-address { font-size: 12px; line-height: 1.35; margin-bottom: 6px; }
  .contact-line {
    display: flex; align-items: center; gap: 7px;
    font-size: 12px; line-height: 1.45;
  }
  .contact-line svg { width: 10px; height: 10px; flex: none; }
  .contact-web { letter-spacing: 2.5px; font-weight: 700; }

  .back-brand {
    position: absolute; top: 108px; right: 60px;
    color: var(--gold); font-size: 44px; font-weight: 400;
    letter-spacing: 1px;
  }
</style>
</head>
<body>
<main class="sheet">

  <section class="card card-front" aria-label="Business card front">
    <svg class="card-shape" viewBox="0 0 525 300" aria-hidden="true">
      <path class="band" d="M0 0 H205 Q30 120 112 300 H0 Z"/>
      <path class="band" d="M420 0 H525 V300 H330 Q520 170 420 0 Z"/>
    </svg>
    <div class="front-brand">Veridan Crest</div>
    <div class="contact">
      <div class="contact-name">ELENA MARSH</div>
      <div class="contact-title">Director</div>
      <div class="contact-address">PO BOX 482, Harbor Street<br>4th Lane, Nevada</div>
      <div class="contact-line">
        <svg viewBox="0 0 10 10" aria-hidden="true"><rect x="0.75" y="0.75" width="8.5" height="8.5" fill="none" stroke="currentColor" stroke-width="1.2"/></svg>
        <span>(555) 210 4870</span>
      </div>
      <div class="contact-line">
        <svg viewBox="0 0 10 10" aria-hidden="true"><rect x="0" y="1.5" width="10" height="7" fill="currentColor"/><path d="M0 1.5 L5 5.5 L10 1.5" fill="none" stroke="#fff" stroke-width="1"/></svg>
        <span>first.last@vc-ppg.com</span>
      </div>
      <div class="contact-line">
        <svg viewBox="0 0 10 10" aria-hidden="true"><circle cx="5" cy="5" r="4.5" fill="currentColor"/><path d="M0.5 5 H9.5 M5 0.5 V9.5 M5 0.5 Q1.8 5 5 9.5 M5 0.5 Q8.2 5 5 9.5" fill="none" stroke="#fff" stroke-width="0.6"/></svg>
        <span class="contact-web">www.vc-ppg.com</span>
      </div>
    </div>
  </section>

  <section class="card card-back" aria-label="Business card back">
    <svg class="card-shape" viewBox="0 0 525 300" aria-hidden="true">
      <path class="band" d="M0 140 Q90 245 300 300 H0 Z"/>
    </svg>
    <div class="back-brand">Veridan Crest</div>
  </section>

</main>
</body>
</html>
```